App Design for Restaurant App

We need a design for the new Mobile App for the Restaurant Velmo. See attachment for presentation sketches.
There are two attached files: File 2 shows the App in general and File 1 shows the five screens which need to be designed. Your work should contain the general color scheme, icons and layout proposal.
Updates
Hi Designers
There where several questions about the scope of the work. We are looking for a design for an App. The promotion website of the restaurant Velmo can be found under www.restaurant-velmo.example
There you will get an impression of the Corporate Identity used by the restaurant and you will also find the logo.
In the sketch there are several screens which don't need a design, e.g. the cover flow or video screen
please ask if you have any question
kind regards
Tobias
Industry/Entity Type
Restaurant
Look and feel
Each slider illustrates characteristics of the customer's brand and the style your logo design should communicate.

```html
<!DOCTYPE html>
<html lang="de">
<head>
<meta charset="utf-8">
<title>Restaurant Velmo – App</title>
<link rel="stylesheet" href="https://fonts.googleapis.com/css2?family=Arimo:wght@400;700&display=swap">
<style>
  :root {
    --page-bg: #2b2b2b;
    --status-bg: #0d0d0d;
    --status-text: #e6e6e6;
    --nav-top: #8a9c55;
    --nav-bottom: #5f7131;
    --nav-title: #f4f4e6;
    --back-top: #9bac68;
    --back-bottom: #6e8040;
    --back-text: #eef2dc;
    --content-edge: #efe68a;
    --content-center: #fbf8c7;
    --photo-frame: #7d8b4c;
    --btn-top: #8b9b58;
    --btn-bottom: #5c6d30;
    --btn-border: #4a5826;
    --btn-text: #ffffff;
  }
  * { box-sizing: border-box; margin: 0; padding: 0; }
  html, body {
    width: 1200px; height: 900px; overflow: hidden;
    background: var(--page-bg);
    font-family: "Arimo", Arial, sans-serif;
  }
  .app-screen {
    position: absolute; left: 316px; top: 25px;
    width: 568px; height: 850px;
    overflow: hidden;
  }
  .status-bar {
    position: relative;
    height: 36px; background: var(--status-bg); color: var(--status-text);
    display: flex; align-items: center; justify-content: space-between;
    padding: 0 14px; font-size: 14px;
  }
  .status-bar .signal, .status-bar .icons { display: flex; align-items: center; gap: 6px; }
  .status-bar .time { position: absolute; left: 0; right: 0; text-align: center; pointer-events: none; }
  .nav-bar {
    position: relative; height: 72px;
    background: linear-gradient(var(--nav-top), var(--nav-bottom));
    display: flex; align-items: center; justify-content: center;
    box-shadow: 0 3px 6px rgba(0,0,0,.25); z-index: 1;
  }
  .nav-title {
    color: var(--nav-title); font-weight: 700; font-size: 24px; letter-spacing: 1px;
    text-shadow: 0 -1px 0 rgba(0,0,0,.35);
  }
  .back-button {
    position: absolute; left: 20px; top: 20px; height: 32px; width: 108px;
    background: linear-gradient(var(--back-top), var(--back-bottom));
    clip-path: polygon(14px 0, 100% 0, 100% 100%, 14px 100%, 0 50%);
    border-radius: 0 6px 6px 0;
    color: var(--back-text); font-size: 20px;
    display: flex; align-items: center; justify-content: center; padding-left: 10px;
  }
  .menu-grid { position: absolute; right: 20px; top: 18px; }
  .content {
    height: 742px;
    background: radial-gradient(ellipse at 50% 45%, var(--content-center) 40%, var(--content-edge) 100%);
    position: relative;
  }
  .hero-photo {
    position: absolute; left: 24px; top: 26px; width: 516px; height: 218px;
    border: 4px solid var(--photo-frame); border-radius: 8px;
    background: linear-gradient(100deg, #c9b79a 0%, #b5412e 30%, #6b4a38 55%, #d9d2c6 75%, #a97a52 100%);
  }
  .menu-list {
    position: absolute; left: 94px; top: 312px; width: 374px;
    list-style: none; display: flex; flex-direction: column; gap: 28px;
  }
  .menu-button {
    display: flex; align-items: center; justify-content: center;
    height: 58px; border-radius: 6px;
    background: linear-gradient(var(--btn-top), var(--btn-bottom));
    border: 1px solid var(--btn-border);
    box-shadow: 0 2px 4px rgba(0,0,0,.3);
    color: var(--btn-text); font-weight: 700; font-size: 24px;
    text-shadow: 0 -1px 0 rgba(0,0,0,.35);
  }
</style>
</head>
<body>
  <main class="app-screen">
    <div class="status-bar">
      <span class="signal">
        <svg width="18" height="12" viewBox="0 0 18 12" aria-hidden="true">
          <rect x="0" y="9" width="3" height="3" fill="#e6e6e6"/>
          <rect x="5" y="6" width="3" height="6" fill="#e6e6e6"/>
          <rect x="10" y="3" width="3" height="9" fill="#e6e6e6"/>
          <rect x="15" y="0" width="3" height="12" fill="#e6e6e6"/>
        </svg>3G
      </span>
      <span class="time">8:30 PM</span>
      <span class="icons">
        <svg width="26" height="12" viewBox="0 0 26 12" aria-label="Akku">
          <rect x="0.5" y="0.5" width="22" height="11" rx="2" fill="none" stroke="#e6e6e6"/>
          <rect x="2.5" y="2.5" width="18" height="7" fill="#e6e6e6"/>
          <rect x="23" y="4" width="2.5" height="4" fill="#e6e6e6"/>
        </svg>
      </span>
    </div>

    <header class="nav-bar">
      <span class="back-button">zurück</span>
      <h1 class="nav-title">RESTAURANT</h1>
      <svg class="menu-grid" width="36" height="36" viewBox="0 0 36 36" aria-label="Menü">
        <g fill="#eef2dc">
          <rect x="0" y="0" width="9" height="9" rx="1.5"/><rect x="13" y="0" width="9" height="9" rx="1.5"/><rect x="26" y="0" width="9" height="9" rx="1.5"/>
          <rect x="0" y="13" width="9" height="9" rx="1.5"/><rect x="13" y="13" width="9" height="9" rx="1.5"/><rect x="26" y="13" width="9" height="9" rx="1.5"/>
          <rect x="0" y="26" width="9" height="9" rx="1.5"/><rect x="13" y="26" width="9" height="9" rx="1.5"/><rect x="26" y="26" width="9" height="9" rx="1.5"/>
        </g>
      </svg>
    </header>

    <section class="content">
      <div class="hero-photo" role="img" aria-label="Foto des Restaurant-Innenraums mit roten Sitzbänken, Holzwänden und gedeckten Tischen"></div>
      <ul class="menu-list">
        <li class="menu-button">Wir stellen uns vor...</li>
        <li class="menu-button">Das Team</li>
        <li class="menu-button">Offnungszeiten</li>
        <li class="menu-button">Kontkt</li>
      </ul>
    </section>
  </main>
</body>
</html>
```